Copperfield Growth Institute is changing lives and needs a state of the art PageLoom Business Web

We are looking for lots of WOW factor. We need a state of the art website that inspires people to take action toward changing their life. We have some award winning trademarked programs that we are looking to introduce through our website.

The Top Portion will have a place holder for a welcome video (currently being recorded) and this brief description of the business along side of it:
=====================================================
Let’s face it. Life is hard. Being human isn’t easy for any of us. Here, at the Copperfield Growth Institute, we understand that simple truth. We know that having a strong self-worth first requires you to be aware of your value as a Human Being. Human potential is the HIGHEST value that creation has to offer.

Regardless of whether you see it through the eyes of evolution or through the eyes of religion, the truth of the matter is that Human Beings are of significant value. Abundance is our birthright! Our focus is on developing that human potential.

There is only one thing holding you back from experiencing overflowing abundance – YOU! Ask yourself, why haven’t I experienced that true transformation, in my life, that attracts abundance?

What if there was a way to remove the uncertainty tied to the labyrinth of life? What if you no longer have to be a victim of the unpredictable? Well, the good news is – Its Possible! There is an amazing amount of potential locked away deep inside you. Potential that has the capacity to release you from your current patterns of thinking and launch a complete turning point in your life.

The Copperfield Growth Institute recognizes this potential, often before you recognize it in yourself, and is excited to partner with you on your journey to becoming an unstoppable force. We look forward to resourcing you with the tools and training that will help you synchronize your desire and your direction with your destiny!
============================================================

Under the welcome / intro block, we would like to have a gallery that scrolls through pictures, and inspirational quotes. We can also use this to advertise
our services and special deals on programs.

Next section can outline our lanes of business or focus areas:

High Performance Living
Business Coaching & Consultancy
Digital Resources Center

Here is the template we would like to leverage: https://pageloom-sites.example/theme/harvestline
or you can be creative and provide one you think would work best....

Should have some awesome photos, descriptions, etc....

Here are some samples to model after:

https://velmorabox.example/
https://www.kv7-mentoring.example/
http://derekosgoodby.example/

https://fenwickroutecrew.example/talk/?c=fnwk-se-bo&frtc=frt-core&gclid=QzXbTkLmNpRsVwYa-93tyhhb7RTKcPMqVTzZTwLo-QRAPiZAxHzT_K_QzXB

https://orlando-tebbit.example/
https://www.thecortexloft.example/
https://www.hollisvane.example/

Target Market(s)

Business Leaderships and anyone interested in personal development and growth

Industry/Entity Type

Leadership

Coding

Coded - Design and coding required

Font styles to use
Serif
Sans Serif
Decorative
Script

Colors

Designer to choose colors to be used in the design.

Requirements
Must have
• Business Name, Logo, and brief introduction paragraph. Must have space for the welcome video.
• We do not have any current site but do already own the domain for it:
• https://cgigrow.example/ is the PageLoom site we will be using once we choice a winner to work with
• Must use our Taglines:
• Shaping the existence of individuals, organizations, and communities...
• Turn your days into a rolling parade of wonder!
• =====================================================
• Would like music to softly play in back ground when people land on the page. This song could repeat in the background: https://www.vidstreamr.example/watch?v=QKTw7mZpLxa&list=ZRt4HbWqYcNmKdP8VsLe31JxfTuAoGh2N&index=4
• You can also cycle through the entire soundtrack of the MIDNIGHT CARAVAN - all those songs work perfectly with our themes
• You must also blend the content available on this site with the new site:
• https://www.harlowbrightcircle.example/dorianwexley
Nice to have
• would like music to softly play in back ground when people land on the page. This song could repeat in the softly in the background: https://www.vidstreamr.example/watch?v=QKTw7mZpLxa&list=ZRt4HbWqYcNmKdP8VsLe31JxfTuAoGh2N&index=4
Should not have
• Ads, empty white space, negative perspectives, etc....

```html
<!DOCTYPE html>
<html lang="en">
<head>
<meta charset="utf-8">
<title>Copperfield Growth Institute</title>
<link rel="stylesheet" href="https://fonts.googleapis.com/css2?family=Cinzel:wght@400;700&family=Montserrat:wght@400;600;700&family=Lato:wght@400;700&display=swap">
<style>
:root{
  --navy:#2b2866;
  --purple:#3a3584;
  --purple-light:#4d48a0;
  --ink:#3a3a46;
  --muted:#6b6b78;
  --paper:#ffffff;
  --mist:#ececef;
  --footer:#2e2e33;
}
*{box-sizing:border-box;margin:0;padding:0}
html,body{width:1200px;height:3488px;overflow:hidden}
body{position:relative;background:var(--mist);font-family:"Lato",sans-serif;color:var(--ink)}
.abs{position:absolute}

/* header */
.site-header{left:0;top:0;width:1200px;height:122px;background:var(--paper)}
.support{left:160px;top:18px;display:flex;align-items:center;gap:12px}
.support-icon{width:40px;height:40px;border-radius:50%;background:var(--navy);display:flex;align-items:center;justify-content:center}
.support-text{font-family:"Montserrat",sans-serif;color:var(--navy);font-size:15px;font-weight:700;line-height:1.25}
.support-text span{display:block;font-weight:400;font-size:14px}
.brand{left:420px;top:10px;width:360px;text-align:center;display:flex;flex-direction:column;align-items:center;gap:4px}
.brand-mark{width:30px;height:30px;border-radius:50%;background:var(--navy)}
.brand-name{font-family:"Cinzel",serif;font-weight:700;color:var(--navy);font-size:22px;line-height:1.1}
.search{left:790px;top:22px;width:210px;height:30px;border:1px solid #c9c9d4;border-radius:16px;display:flex;align-items:center;padding:0 12px;gap:8px;font-family:"Montserrat",sans-serif;font-size:13px;color:#8a8a96}
.nav{top:94px;font-family:"Montserrat",sans-serif;font-size:15px;color:var(--navy);display:flex;gap:36px}
.nav-left{left:118px}
.nav-right{left:742px}

/* hero */
.hero{left:0;top:122px;width:1200px;height:620px;overflow:hidden}
.hero-photo{position:absolute;inset:0;background:linear-gradient(180deg,#8f8fbf 0%,#6b6aa3 35%,#3b3978 70%,#1d1b45 100%)}
.hero-play{left:572px;top:172px;width:56px;height:40px;border-radius:10px;background:#fff}
.hero-title{left:0;top:230px;width:1200px;text-align:center;font-family:"Cinzel",serif;color:#fff;font-size:58px;line-height:1.05}
.hero-tag{left:0;top:380px;width:1200px;text-align:center;font-family:"Montserrat",sans-serif;font-weight:600;color:#fff;font-size:26px}
.hero-curve{left:0;top:560px}
.hero-badge{left:560px;top:680px;width:80px;height:80px;border-radius:50%;background:var(--paper);border:4px solid var(--purple);display:flex;align-items:center;justify-content:center}
.hero-badge span{width:44px;height:44px;border-radius:50%;background:var(--navy)}

/* welcome */
.welcome{left:0;top:742px;width:1200px;height:740px;background:var(--paper)}
.welcome-globe{left:100px;top:86px;width:340px;height:340px;border-radius:50%;background:radial-gradient(circle at 45% 40%,#e9e4f2 0%,#9c8fc2 45%,#3a3584 80%,#ffffff 81%)}
.welcome-copy{left:488px;top:88px;width:620px}
.welcome-title{font-family:"Cinzel",serif;color:var(--navy);font-size:34px;font-weight:700;line-height:1.1}
.welcome-sub{font-family:"Cinzel",serif;color:var(--navy);font-size:28px;margin-bottom:16px}
.body-text{font-family:"Lato",sans-serif;font-size:14.5px;line-height:1.62;color:var(--muted)}
.body-text p{margin-bottom:10px}
.welcome-more{left:100px;top:450px;width:1000px}

/* gallery */
.gallery-wave{left:0;top:1420px}
.gallery{left:0;top:1700px;width:1200px;height:620px;background:var(--purple)}
.gallery-title{left:0;top:44px;width:1200px;text-align:center;font-family:"Montserrat",sans-serif;font-weight:600;color:#fff;font-size:30px;letter-spacing:1px}
.grid{left:220px;top:88px;display:grid;grid-template-columns:repeat(3,252px);gap:18px 22px}
.tile{width:252px}
.tile-img{height:170px}
.tile-cap{height:30px;background:#26234f;color:#fff;font-family:"Montserrat",sans-serif;font-weight:700;font-size:13px;display:flex;align-items:center;padding-left:12px}
.t1{background:linear-gradient(180deg,#a9c7e8,#2d5a8a)}
.t2{background:linear-gradient(180deg,#1b2a4c,#5c7fb0)}
.t3{background:linear-gradient(180deg,#f1f0ec,#c9c6bc)}
.t4{background:linear-gradient(180deg,#e8b77b,#5d6f8a)}
.t5{background:linear-gradient(180deg,#4f8ac4,#1f3560)}
.t6{background:linear-gradient(180deg,#e5b638,#3e2d12)}
.dots{left:558px;top:550px;display:flex;gap:12px}
.dots span{width:16px;height:16px;border-radius:50%;border:2px solid #fff}
.dots span.on{background:#fff}
.gallery-wave-bottom{left:0;top:2318px}

/* lanes */
.lanes-title{left:0;top:2450px;width:1200px;text-align:center;font-family:"Montserrat",sans-serif;font-weight:700;color:var(--navy);font-size:32px}
.card{top:2528px;width:322px;height:360px;background:var(--paper);border:3px solid var(--purple);text-align:center;padding:40px 30px 0}
.card-icon{width:80px;height:80px;margin:0 auto 36px;border-radius:50%;border:3px solid var(--navy);display:flex;align-items:center;justify-content:center}
.card-title{font-family:"Montserrat",sans-serif;font-weight:700;color:var(--navy);font-size:16px;line-height:1.4;margin-bottom:16px}
.card-text{font-size:13.5px;line-height:1.6;color:var(--muted)}

/* footer */
.footer-curve{left:0;top:2930px}
.footer{left:0;top:3030px;width:1200px;height:458px;background:var(--footer)}
.footer-brand{left:400px;top:-30px;width:400px;display:flex;flex-direction:column;align-items:center;gap:6px}
.footer-brand .brand-mark{background:#fff}
.footer-brand .brand-name{color:#fff;font-size:30px}
.contacts{left:100px;top:120px;width:1000px;display:flex;justify-content:space-between}
.contact{width:300px;text-align:center;color:#fff;font-family:"Cinzel",serif;font-size:16px;line-height:1.5}
.contact-icon{width:64px;height:64px;border-radius:50%;background:var(--purple);margin:0 auto 16px;display:flex;align-items:center;justify-content:center}
.social{left:540px;top:270px;display:flex;gap:10px}
.social span{width:28px;height:28px;border-radius:50%;border:2px solid #fff}
.footer-nav{left:0;top:344px;width:1200px;text-align:center;font-family:"Montserrat",sans-serif;color:#fff;font-size:15px;letter-spacing:1px}
.footer-nav span{margin:0 16px}
.copyright{left:0;top:400px;width:1200px;text-align:center;color:#bdbdc6;font-size:14px}
</style>
</head>
<body>

<header class="site-header abs">
  <div class="support abs">
    <div class="support-icon">
      <svg width="20" height="20" viewBox="0 0 24 24"><path fill="#fff" d="M6.6 10.8a15.1 15.1 0 0 0 6.6 6.6l2.2-2.2a1 1 0 0 1 1-.25 11.4 11.4 0 0 0 3.6.57 1 1 0 0 1 1 1V20a1 1 0 0 1-1 1A17 17 0 0 1 3 4a1 1 0 0 1 1-1h3.5a1 1 0 0 1 1 1c0 1.25.2 2.45.57 3.57a1 1 0 0 1-.25 1z"/></svg>
    </div>
    <div class="support-text">SUPPORT CALL US<span>555 010 2244</span></div>
  </div>
  <div class="brand abs">
    <span class="brand-mark"></span>
    <div class="brand-name">Copperfield Growth Institute</div>
  </div>
  <div class="search abs">
    <svg width="14" height="14" viewBox="0 0 24 24"><circle cx="10" cy="10" r="7" fill="none" stroke="#8a8a96" stroke-width="2.5"/><path d="M15 15l6 6" stroke="#8a8a96" stroke-width="2.5"/></svg>
    SEARCH
  </div>
  <nav class="nav nav-left abs"><span>Home</span><span>About Us</span><span>Gallery</span></nav>
  <nav class="nav nav-right abs"><span>Our Services</span><span>Blog</span><span>Contact</span></nav>
</header>

<section class="hero abs">
  <div class="hero-photo" role="img" aria-label="Silhouettes of people climbing a mountain ridge at dusk, placeholder for the welcome video"></div>
  <div class="hero-play abs">
    <svg width="56" height="40" viewBox="0 0 56 40"><path d="M22 12l14 8-14 8z" fill="#2b2866"/></svg>
  </div>
  <h1 class="hero-title abs">Copperfield<br>Growth Institute</h1>
  <p class="hero-tag abs">Shaping the existence of individuals, organizations, and communities...</p>
  <svg class="hero-curve abs" width="1200" height="60" viewBox="0 0 1200 60">
    <path d="M0 60V10Q600 80 1200 10V60Z" fill="#fff"/>
    <path d="M0 14Q600 84 1200 14" fill="none" stroke="#3a3584" stroke-width="8"/>
  </svg>
</section>

<section class="welcome abs">
  <div class="welcome-globe abs" role="img" aria-label="Globe made of portrait tiles of people"></div>
  <div class="welcome-copy abs">
    <h2 class="welcome-title">Welcome to Copperfield</h2>
    <div class="welcome-sub">Growth Institute</div>
    <div class="body-text">
      <p>Let’s face it. Life is hard. Being human isn’t easy for any of us. Here, at the Copperfield Growth Institute, we understand that simple truth. We know that having a strong self-worth first requires you to be aware of your value as a Human Being. Human potential is the HIGHEST value that creation has to offer.</p>
      <p>Regardless of whether you see it through the eyes of evolution or through the eyes of religion, the truth of the matter is that Human Beings are of significant value. Abundance is our birthright! Our focus is on developing that human potential.</p>
    </div>
  </div>
  <div class="welcome-more body-text abs">
    <p>There is only one thing holding you back from experiencing overflowing abundance – YOU! Ask yourself, why haven’t I experienced that true transformation, in my life, that attracts abundance? What if there was a way to remove the uncertainty tied to the labyrinth of life? What if you no longer have to be a victim of the unpredictable? Well, the good news is – Its Possible! There is an amazing amount of potential locked away deep inside you. Potential that has the capacity to release you from your current patterns of thinking and launch a complete turning point in your life.</p>
    <p>The Copperfield Growth Institute recognizes this potential, often before you recognize it in yourself, and is excited to partner with you on your journey to becoming an unstoppable force. We look forward to resourcing you with the tools and training that will help you synchronize your desire and your direction with your destiny!</p>
  </div>
</section>

<svg class="gallery-wave abs" width="1200" height="290" viewBox="0 0 1200 290">
  <path d="M0 60Q600 -20 1200 70V290H0Z" fill="#d9d9de"/>
  <path d="M0 160Q700 60 1200 150V290H0Z" fill="#3a3584"/>
</svg>
<section class="gallery abs">
  <h2 class="gallery-title abs">GALLERY</h2>
  <div class="grid abs">
    <div class="tile"><div class="tile-img t1" role="img" aria-label="Group jumping in silhouette against the sky"></div><div class="tile-cap">SED UT PERSPICIATIS UNDE</div></div>
    <div class="tile"><div class="tile-img t2" role="img" aria-label="Figure holding a trophy on a mountain top"></div><div class="tile-cap">SED UT PERSPICIATIS UNDE</div></div>
    <div class="tile"><div class="tile-img t3" role="img" aria-label="Business people shaking hands"></div><div class="tile-cap">SED UT PERSPICIATIS UNDE</div></div>
    <div class="tile"><div class="tile-img t4" role="img" aria-label="Hiker on a summit at sunrise"></div><div class="tile-cap">SED UT PERSPICIATIS UNDE</div></div>
    <div class="tile"><div class="tile-img t5" role="img" aria-label="Hand touching a digital network screen"></div><div class="tile-cap">SED UT PERSPICIATIS UNDE</div></div>
    <div class="tile"><div class="tile-img t6" role="img" aria-label="Figure climbing toward a goal sign"></div><div class="tile-cap">SED UT PERSPICIATIS UNDE</div></div>
  </div>
  <div class="dots abs"><span></span><span class="on"></span><span class="on"></span></div>
</section>
<svg class="gallery-wave-bottom abs" width="1200" height="80" viewBox="0 0 1200 80">
  <path d="M0 0H1200V10Q600 90 0 20Z" fill="#3a3584"/>
</svg>

<h2 class="lanes-title abs">OUR LANES OF BUSINESS OR FOCUS AREAS:</h2>
<article class="card abs" style="left:100px">
  <div class="card-icon"><svg width="36" height="36" viewBox="0 0 24 24"><path d="M4 20V12M10 20V8M16 20V4M2 20h20" stroke="#2b2866" stroke-width="2.4" fill="none"/></svg></div>
  <h3 class="card-title">HIGH PERFORMANCE<br>LIVING</h3>
  <p class="card-text">Build daily habits that sharpen focus, lift energy and sustain lasting personal momentum.</p>
</article>
<article class="card abs" style="left:439px">
  <div class="card-icon"><svg width="36" height="36" viewBox="0 0 24 24"><circle cx="12" cy="8" r="4" fill="#2b2866"/><path d="M4 21a8 8 0 0 1 16 0z" fill="#2b2866"/></svg></div>
  <h3 class="card-title">BUSINESS COACHING &amp;<br>CONSULTANCY</h3>
  <p class="card-text">Guidance for leaders and teams to clarify vision, align strategy and grow with purpose.</p>
</article>
<article class="card abs" style="left:778px">
  <div class="card-icon"><svg width="36" height="36" viewBox="0 0 24 24"><rect x="3" y="4" width="18" height="12" rx="1" fill="none" stroke="#2b2866" stroke-width="2.2"/><path d="M8 20h8M12 16v4" stroke="#2b2866" stroke-width="2.2"/></svg></div>
  <h3 class="card-title">DIGITAL RESOURCES<br>CENTER</h3>
  <p class="card-text">Courses, guides and tools you can access anytime to keep your growth moving forward.</p>
</article>

<svg class="footer-curve abs" width="1200" height="110" viewBox="0 0 1200 110">
  <path d="M0 70Q600 -10 1200 70V110H0Z" fill="#2e2e33"/>
  <path d="M0 62Q600 -18 1200 62" fill="none" stroke="#3a3584" stroke-width="8"/>
</svg>
<footer class="footer abs">
  <div class="footer-brand abs">
    <span class="brand-mark"></span>
    <div class="brand-name">Copperfield Growth Institute</div>
  </div>
  <div class="contacts abs">
    <div class="contact">
      <div class="contact-icon"><svg width="26" height="26" viewBox="0 0 24 24"><path d="M12 2a7 7 0 0 0-7 7c0 5 7 13 7 13s7-8 7-13a7 7 0 0 0-7-7zm0 9.5A2.5 2.5 0 1 1 12 6.5a2.5 2.5 0 0 1 0 5z" fill="#fff"/></svg></div>
      418 Alder Row, Easton Vale<br>Harbor Province - K2M 4T7
    </div>
    <div class="contact">
      <div class="contact-icon"><svg width="24" height="24" viewBox="0 0 24 24"><path fill="#fff" d="M6.6 10.8a15.1 15.1 0 0 0 6.6 6.6l2.2-2.2a1 1 0 0 1 1-.25 11.4 11.4 0 0 0 3.6.57 1 1 0 0 1 1 1V20a1 1 0 0 1-1 1A17 17 0 0 1 3 4a1 1 0 0 1 1-1h3.5a1 1 0 0 1 1 1c0 1.25.2 2.45.57 3.57a1 1 0 0 1-.25 1z"/></svg></div>
      Phone:<br>555 010 2244
    </div>
    <div class="contact">
      <div class="contact-icon"><svg width="26" height="26" viewBox="0 0 24 24"><rect x="3" y="5" width="18" height="14" rx="1" fill="none" stroke="#fff" stroke-width="2"/><path d="M3 6l9 7 9-7" fill="none" stroke="#fff" stroke-width="2"/></svg></div>
      Email:<br>hello@cgigrow.example
    </div>
  </div>
  <div class="social abs"><span></span><span></span><span></span><span></span></div>
  <nav class="footer-nav abs"><span>HOME</span>|<span>ABOUT US</span>|<span>OUR GALLERY</span>|<span>OUR SERVICES</span>|<span>CONTACT US</span></nav>
  <p class="copyright abs">© 2019 Copperfield Growth Institute. All right reserved</p>
</footer>

</body>
</html>
```